13 Tavo - new website design project

Our company Tavo Electrical is developing a new lead generation website focused on Electrical, LED Lighting and Solar Power. We need a high converting website.

Example of our current website is www.tavoelectrical.com.au You can take content from this website for this new design. Our colours are red, black and white. For our new website we would like to promote Tavo, Bright Days Ahead. Please listen to the jingle.

The below link is the company jingle that we have developed.
http://www.tunecraftaudio.com.au/tav-tc-v1/

The key for this brief is to generate leads for Electrical, LED Lighting (for commercial) and Solar Power & Storage.

Target Market(s)

Business owners in Melbourne Victoria

Number of Pages Required

4 page

Colors
ec1f27
ffffff

Requirements
Must have
• This page must be clean, be in line with company branding and a high converting lead website.

```html
<!DOCTYPE html>
<html lang="en">
<head>
<meta charset="utf-8">
<title>Tavo Electrical – Electrical, LED Lighting &amp; Solar Power</title>
<link href="https://fonts.googleapis.com/css2?family=Audiowide&family=Open+Sans:ital,wght@0,400;0,600;0,700;1,400&family=Rajdhani:wght@600;700&display=swap" rel="stylesheet">
<style>
:root{
  --red:#ec1f27;
  --red-dark:#c4161d;
  --black:#1d1d1f;
  --charcoal:#2e2f33;
  --grey-bg:#f3f3f3;
  --line:#b9b9b9;
  --text:#333;
  --muted:#777;
  --white:#fff;
}
*{box-sizing:border-box;margin:0;padding:0}
html,body{width:1200px;height:3614px;overflow:hidden}
body{font-family:"Open Sans",Arial,sans-serif;color:var(--text);background:var(--white);position:relative}
.sec{position:absolute;left:0;width:1200px}
.heading{font-family:"Audiowide",sans-serif;font-weight:400;text-transform:uppercase;text-align:center;font-size:31px;letter-spacing:1px;color:var(--black)}
.heading .hl{color:var(--red)}
.btn-outline{display:inline-block;border:2px solid var(--black);font-size:12px;font-weight:600;padding:9px 22px;transform:skewX(-15deg);color:var(--black);background:var(--white)}
.btn-outline span{display:inline-block;transform:skewX(15deg)}

/* header */
.site-header{top:0;height:108px;background:var(--white)}
.brand{position:absolute;left:145px;top:16px}
.brand-name{font-family:"Audiowide",sans-serif;font-size:38px;color:var(--red);line-height:1}
.brand-tag{font-size:12px;font-weight:600;color:var(--black);margin-top:6px}
.header-tag{position:absolute;left:0;width:1200px;top:38px;text-align:center;font-style:italic;font-size:16px;color:var(--black);line-height:1.3}
.header-tag b{font-weight:700}
.phone{position:absolute;display:flex;align-items:center;gap:8px}
.phone .num{font-family:"Rajdhani",sans-serif;font-weight:700;font-size:40px;line-height:1}
.phone .num .d{color:var(--black)}
.phone .num .r{color:var(--red)}
.header-phone{right:140px;top:32px}

/* nav */
.main-nav{top:108px;height:52px;background:var(--charcoal)}
.main-nav ul{list-style:none;display:flex;position:absolute;left:140px;top:17px;gap:26px}
.main-nav li{font-family:"Rajdhani",sans-serif;font-weight:700;font-size:13px;text-transform:uppercase;color:var(--white)}
.main-nav li.active{color:var(--red)}
.service-tabs{position:absolute;right:140px;top:0;height:52px;display:flex;background:var(--red);padding:0 6px 0 30px;clip-path:polygon(22px 0,100% 0,100% 100%,0 100%)}
.service-tabs span{font-family:"Rajdhani",sans-serif;font-weight:700;font-size:13px;color:var(--white);padding:17px 20px;text-transform:uppercase}

/* hero */
.hero{top:160px;height:505px;background:linear-gradient(90deg,#3a3a3a,#555 45%,#3d3d3d)}
.hero-shade{position:absolute;inset:0;background:rgba(0,0,0,.35)}
.hero-photo{position:absolute;left:142px;top:60px;width:398px;height:398px;border-radius:50%;background:radial-gradient(circle at 40% 40%,#b7a88c,#6e6656 60%,#3c3c3c)}
.hero-copy{position:absolute;left:560px;top:130px;width:500px;color:var(--white)}
.hero-copy h1{font-family:"Audiowide",sans-serif;font-weight:400;font-size:36px;margin-bottom:8px}
.hero-copy p{font-size:14px;line-height:1.6;margin-bottom:24px}
.hero .btn-outline{border-color:var(--white);background:transparent;color:var(--white)}
.arrow{position:absolute;top:228px;width:36px;height:44px;background:rgba(255,255,255,.25);display:flex;align-items:center;justify-content:center}
.arrow.l{left:0}.arrow.r{right:0}

/* services */
.services{top:665px;height:520px}
.services-band{position:absolute;left:0;top:0}
.services .heading{position:absolute;top:90px;width:1200px;color:var(--white)}
.service-card{position:absolute;top:142px;width:290px;text-align:center}
.service-img{height:193px}
.service-card h3{font-family:"Open Sans",sans-serif;font-size:19px;font-weight:600;color:var(--black);margin:14px 0 6px}
.service-card p{font-size:9.5px;line-height:1.5;color:var(--muted);margin-bottom:12px;text-align:left;padding:0 6px}
.service-card .btn-outline{font-size:10px;padding:6px 18px}

/* who */
.who{top:1241px;height:410px;background:var(--grey-bg)}
.who-copy{position:absolute;left:145px;top:103px;width:480px}
.who-copy h2{font-family:"Audiowide",sans-serif;font-weight:400;font-size:28px;text-transform:uppercase;color:var(--black);margin-bottom:6px}
.who-copy h2 .hl{color:var(--red)}
.who-copy p{font-size:13px;line-height:1.6;color:var(--red-dark);margin-bottom:20px}
.laptop{position:absolute;left:612px;top:72px}
.laptop-brand{position:absolute;left:0;width:100%;top:92px;text-align:center}
.laptop-brand .n{font-family:"Audiowide",sans-serif;font-size:48px;color:var(--black);line-height:1}
.laptop-brand .t{font-size:14px;font-weight:600;color:var(--red);margin-top:6px}
.play{position:absolute;left:370px;top:30px;width:76px;height:76px;border-radius:50%;background:var(--red);color:var(--white);font-size:10px;font-weight:700;display:flex;flex-direction:column;align-items:center;justify-content:center;gap:4px}

/* why */
.why{top:1687px;height:480px}
.why .heading{position:absolute;top:50px;width:1200px}
.why-box{position:absolute;border:1px solid var(--line);background:var(--white)}
.why-box h4{font-size:12px;font-weight:700;text-transform:uppercase;color:var(--black);margin-bottom:4px}
.why-box p{font-size:9.5px;line-height:1.45;color:var(--text)}
.why-box.left{text-align:right;padding:12px 64px 10px 16px}
.why-box.right{text-align:left;padding:12px 16px 10px 64px}
.why-icon{position:absolute;top:50%;margin-top:-24px;width:48px;height:48px;border-radius:50%;background:var(--white);display:flex;align-items:center;justify-content:center}
.why-box.left .why-icon{right:-25px}
.why-box.right .why-icon{left:-25px}
.why-cta{position:absolute;right:145px;top:372px;display:flex;align-items:center;gap:12px}
.btn-red{display:inline-block;background:var(--red);color:var(--white);font-family:"Rajdhani",sans-serif;font-weight:700;font-size:14px;padding:11px 30px;transform:skewX(-15deg);text-transform:uppercase}
.btn-red span{display:inline-block;transform:skewX(15deg)}

/* clients */
.clients{top:2198px;height:467px;background:linear-gradient(90deg,#2d2d2f,#4a4a4c 55%,#333)}
.clients-shade{position:absolute;inset:0;background:rgba(0,0,0,.3)}
.clients .heading{position:absolute;top:62px;width:1200px;color:var(--white)}
.testimonial{position:absolute;left:205px;top:115px;width:790px;height:212px;background:var(--white);border-radius:22px}
.testimonial::after{content:"";position:absolute;left:380px;bottom:-18px;border:18px solid transparent;border-bottom:0;border-top-color:var(--white)}
.testi-photo{position:absolute;left:60px;top:24px;width:242px;height:168px;background:linear-gradient(180deg,#7d8a93,#4c555c)}
.view{position:absolute;left:36px;top:12px;width:52px;height:52px;border-radius:50%;background:var(--red);color:var(--white);font-size:9px;font-weight:700;display:flex;flex-direction:column;align-items:center;justify-content:center}
.testi-brand{position:absolute;left:323px;top:48px;font-size:22px;font-weight:600;color:#2a8fc7;display:flex;align-items:center;gap:8px}
.testi-brand i{display:inline-block;width:20px;height:20px;border-radius:50%;border:2px solid #888}
.testi-text{position:absolute;left:323px;top:100px;width:430px;font-style:italic;font-size:13.5px;line-height:1.55;color:var(--black)}
.testi-name{position:absolute;top:370px;width:1200px;text-align:center;color:var(--white)}
.testi-name b{font-size:15px;display:block}
.testi-name span{font-size:10px}
.carousel-arrow{position:absolute;top:198px;font-size:44px;color:rgba(255,255,255,.7);font-weight:300}

/* logos */
.logos{top:2665px;height:150px;background:var(--grey-bg);display:flex;align-items:center;justify-content:center;gap:18px}
.and-more{font-family:"Audiowide",sans-serif;font-size:24px;color:var(--black);line-height:1;margin-right:8px}
.logo-tile{width:130px;height:74px;display:flex;align-items:center;justify-content:center;font-size:16px;font-weight:700;text-align:center;padding:0 8px}
.logo-tile.light{background:var(--white);color:var(--black)}
.logo-tile.soft{background:#ddd;color:#7a1a1a}
.logo-tile.dark{background:#3b3b3b;color:var(--white)}

/* contact */
.contact{top:2815px;height:535px}
.contact .heading{position:absolute;top:100px;width:1200px}
.field{position:absolute;height:38px;border:1px solid #aaa;font-size:10px;color:#888;padding:11px 10px}
.field.select::after{content:"";position:absolute;right:12px;top:15px;border:5px solid transparent;border-top-color:#555}
.contact .btn-red{position:absolute;left:505px;top:383px;font-size:12px;padding:12px 32px}

/* info strip */
.info{top:3330px;height:157px}
.info-bg{position:absolute;left:0;top:0}
.info-item{position:absolute;top:64px;display:flex;align-items:center;gap:12px}
.info-ico{width:56px;height:56px;border-radius:50%;border:3px solid var(--black);display:flex;align-items:center;justify-content:center}
.info-item h5{font-family:"Rajdhani",sans-serif;font-weight:700;font-size:16px;color:var(--red);text-transform:uppercase}
.info-item p{font-size:12px;line-height:1.35;color:var(--black)}
.call-label{font-family:"Rajdhani",sans-serif;font-weight:700;font-size:16px;color:var(--red);border:3px solid var(--black);border-radius:50%;width:56px;height:56px;display:flex;align-items:center;justify-content:center}

/* footer */
.footer-nav{top:3487px;height:48px;background:var(--charcoal)}
.footer-nav ul{list-style:none;display:flex;gap:24px;position:absolute;left:145px;top:16px}
.footer-nav li{font-family:"Rajdhani",sans-serif;font-weight:700;font-size:12px;color:var(--white);text-transform:uppercase}
.footer-nav li.plain{font-family:"Open Sans",sans-serif;font-weight:400;text-transform:none;font-size:11px}
.social{position:absolute;right:140px;top:0;height:48px;width:110px;background:var(--black);clip-path:polygon(20px 0,100% 0,100% 100%,0 100%);display:flex;align-items:center;justify-content:center;gap:10px}
.social i{width:12px;height:12px;background:var(--white);display:block}
.social i.c{border-radius:50%}
.copyright{top:3535px;height:79px;background:var(--black);color:#aaa;font-size:9px;text-align:center;padding-top:34px}
</style>
</head>
<body>

<header class="sec site-header">
  <div class="brand">
    <div class="brand-name">Tavo</div>
    <div class="brand-tag">Bright Days Ahead</div>
  </div>
  <div class="header-tag">Australia's Largest Fully Integrated<br><b>Electrical &amp; Energy Solutions Provider</b></div>
  <div class="phone header-phone">
    <svg width="40" height="30" viewBox="0 0 40 30"><path d="M3 10c0-6 34-6 34 0v4h-9v-4c0-2-16-2-16 0v4H3z" fill="#1d1d1f"/><rect x="8" y="14" width="24" height="14" rx="3" fill="#1d1d1f"/><circle cx="20" cy="21" r="4" fill="#fff"/></svg>
    <div class="num"><span class="d">13 </span><span class="r">7260</span></div>
  </div>
</header>

<nav class="sec main-nav">
  <ul><li class="active">Home</li><li>Tavo Story</li><li>Our Work</li><li>Contact Us</li></ul>
  <div class="service-tabs"><span>Electrical</span><span>LED Lighting</span><span>Solar Power</span></div>
</nav>

<section class="sec hero">
  <div class="hero-shade"></div>
  <div class="hero-photo" role="img" aria-label="Electrician in hard hat and hi-vis vest in front of a switchboard"></div>
  <div class="hero-copy">
    <h1>Electrical Service</h1>
    <p>Lorem ipsum dolor sit amet, consectetur adipiscing elit. Pellentesque dapibus dolor luctus sapien pharetra consectetur. Sed semper nunc quis justo lobortis ultricies. Etiam consectetur sem tortor, sit amet hendrerit turpis suscipit sed vestibulum nec augue in nulla luctus tristique fermentum pulvinar eget fringilla suscipit.</p>
    <span class="btn-outline"><span>learn more ›</span></span>
  </div>
  <div class="arrow l"><svg width="14" height="20"><path d="M11 2 3 10l8 8" stroke="#fff" stroke-width="3" fill="none"/></svg></div>
  <div class="arrow r"><svg width="14" height="20"><path d="M3 2l8 8-8 8" stroke="#fff" stroke-width="3" fill="none"/></svg></div>
</section>

<section class="sec services">
  <svg class="services-band" width="1200" height="300"><polygon points="0,0 1200,0 1200,215 0,300" fill="#ec1f27"/><polygon points="0,300 1200,215 1200,300" fill="#fff"/></svg>
  <h2 class="heading">What We Do</h2>
  <div class="service-card" style="left:145px">
    <div class="service-img" role="img" aria-label="Electrician working on a switchboard" style="background:linear-gradient(135deg,#c9b27a,#6f7c86)"></div>
    <h3>Electrical</h3>
    <p>Lorem ipsum dolor sit amet, consectetur adipiscing elit. Aliquam ullamcorper posuere leo eu dignissim suspendisse orci turpis, consectetur sit amet finibus vitae blandit. Etiam sodales, purus eu sagittis lacinia, sapien eros feugiat ex, id malesuada felis dolor eget mauris donec turpis.</p>
    <span class="btn-outline"><span>learn more ›</span></span>
  </div>
  <div class="service-card" style="left:458px">
    <div class="service-img" role="img" aria-label="Close-up of a bright LED bulb cluster" style="background:radial-gradient(circle,#f4f4f4,#9a9a9a 55%,#2c2c2c)"></div>
    <h3>LED Lighting</h3>
    <p>Cras mattis odio sed sodales volutpat. Nam et ex nec nibh suscipit condimentum. Vivamus tincidunt nisi est, nec facilisis lacus commodo faucibus. Nunc euismod mauris in sapien posuere hendrerit eu at lacus. Fusce cursus varius ipsum sit amet ultricies risus libero mollis dignissim auctor.</p>
    <span class="btn-outline"><span>learn more ›</span></span>
  </div>
  <div class="service-card" style="left:769px">
    <div class="service-img" role="img" aria-label="Rooftop solar panels being installed" style="background:linear-gradient(160deg,#8fb4d8,#2f5f9e 55%,#1e3d6e)"></div>
    <h3>Solar Power</h3>
    <p>Nam placerat volutpat ultricies. Integer fringilla faucibus dui, eget venenatis nulla. Nulla viverra pulvinar sapien, id blandit sem dapibus vel. Donec non risus sit amet lorem pulvinar vulputate vel sed elit. Sed tempus massa et dui congue, et consequat lorem pharetra maximus convallis nunc.</p>
    <span class="btn-outline"><span>learn more ›</span></span>
  </div>
</section>

<section class="sec who">
  <div class="who-copy">
    <h2>Who <span class="hl">We Are</span></h2>
    <p>Lorem ipsum dolor sit amet, consectetur adipiscing elit. Pellentesque dapibus dolor luctus sapien pharetra consectetur. Sed semper nunc quis justo lobortis ultricies. Etiam consectetur sem tortor, sit amet hendrerit turpis suscipit sed. Vestibulum nec augue in nulla luctus tristique quis fermentum lorem nullam pulvinar lorem eget fringilla suscipit. Curabitur suscipit leo eu turpis cursus auctor fusce auctor osuere hendrerit eu.</p>
    <span class="btn-outline"><span>learn more ›</span></span>
  </div>
  <div class="laptop">
    <svg width="448" height="260" viewBox="0 0 448 260">
      <rect x="30" y="0" width="388" height="238" rx="10" fill="#1d1d1f"/>
      <rect x="42" y="12" width="364" height="214" fill="#fff"/>
      <path d="M0 238h448l-10 16c-2 4-6 6-10 6H20c-4 0-8-2-10-6z" fill="#cfcfcf"/>
      <rect x="184" y="238" width="80" height="6" rx="3" fill="#9a9a9a"/>
    </svg>
    <div class="laptop-brand"><div class="n">Tavo</div><div class="t">Bright Days Ahead</div></div>
    <div class="play"><svg width="22" height="16"><rect width="22" height="16" rx="4" fill="#fff"/><path d="M9 4v8l6-4z" fill="#ec1f27"/></svg>PLAY</div>
  </div>
</section>

<section class="sec why">
  <h2 class="heading">Why <span class="hl">Choose Us</span></h2>
  <div class="why-box left" style="left:145px;top:100px;width:433px;height:96px">
    <h4>Professional Service</h4>
    <p>When you hire a Tavo Electrical Electrician you will get a professional and well-presented Electrician that comes skilled and ready to do the job.</p>
    <div class="why-icon"><svg width="34" height="34" viewBox="0 0 34 34"><circle cx="13" cy="13" r="7" fill="none" stroke="#1d1d1f" stroke-width="4" stroke-dasharray="4 2"/><circle cx="24" cy="24" r="5" fill="none" stroke="#1d1d1f" stroke-width="3" stroke-dasharray="3 2"/></svg></div>
  </div>
  <div class="why-box left" style="left:145px;top:217px;width:433px;height:91px">
    <h4>Value for Money</h4>
    <p>We provide extremely competitive pricing, which means you get value for money on quality that is comparable to the best in the industry.</p>
    <div class="why-icon"><svg width="34" height="34" viewBox="0 0 34 34"><circle cx="17" cy="17" r="15" fill="none" stroke="#1d1d1f" stroke-width="3"/><text x="17" y="24" text-anchor="middle" font-family="Open Sans" font-weight="700" font-size="18" fill="#1d1d1f">$</text></svg></div>
  </div>
  <div class="why-box left" style="left:145px;top:318px;width:433px;height:92px">
    <h4>Fully Insured</h4>
    <p>Tavo Electrical is fully insured and equipped to handle break downs and service call outs.</p>
    <div class="why-icon"><svg width="30" height="34" viewBox="0 0 30 34"><path d="M15 2 3 7v9c0 8 5 13 12 16 7-3 12-8 12-16V7z" fill="#1d1d1f"/><path d="M9 17l4 4 8-8" stroke="#fff" stroke-width="3" fill="none"/></svg></div>
  </div>
  <div class="why-box right" style="left:615px;top:100px;width:441px;height:115px">
    <h4>5 Year Workmanship Guarantee</h4>
    <p>You can buy with confidence as all of our work has a 5 year workmanship guarantee. For your peace of mind, we unconditionally back our electrical work. We will come back to fix any problems at our own expense.</p>
    <div class="why-icon"><svg width="32" height="32" viewBox="0 0 32 32"><path d="M5 5l22 22M27 5 5 27" stroke="#1d1d1f" stroke-width="4" stroke-linecap="round"/></svg></div>
  </div>
  <div class="why-box right" style="left:615px;top:237px;width:441px;height:110px">
    <h4>Environmentally Friendly</h4>
    <p>We a committed to reducing carbon emissions by installing Solar Power and upgrading sites to LED Lighting. In addition to reducing the carbon emissions we recycle Fluorescent Tubes, Highbay Globes, Metal and Cardboard.</p>
    <div class="why-icon"><svg width="40" height="40" viewBox="0 0 40 40"><circle cx="20" cy="20" r="19" fill="#1d1d1f"/><path d="M11 28C11 16 20 11 30 11c0 11-7 17-19 17z" fill="#fff"/></svg></div>
  </div>
  <div class="why-cta">
    <div class="phone" style="position:static">
      <svg width="40" height="30" viewBox="0 0 40 30"><path d="M3 10c0-6 34-6 34 0v4h-9v-4c0-2-16-2-16 0v4H3z" fill="#1d1d1f"/><rect x="8" y="14" width="24" height="14" rx="3" fill="#1d1d1f"/><circle cx="20" cy="21" r="4" fill="#fff"/></svg>
      <div class="num"><span class="d">13 </span><span class="r">7260</span></div>
    </div>
    <span class="btn-red"><span>Contact Us ›</span></span>
  </div>
</section>

<section class="sec clients">
  <div class="clients-shade"></div>
  <h2 class="heading">Our <span class="hl">Satisfied Clients</span></h2>
  <div class="carousel-arrow" style="left:142px">‹</div>
  <div class="carousel-arrow" style="right:142px">›</div>
  <div class="testimonial">
    <div class="testi-photo" role="img" aria-label="Interior of a large industrial warehouse with high-bay lighting"></div>
    <div class="view"><svg width="14" height="14"><circle cx="6" cy="6" r="4" stroke="#fff" stroke-width="2" fill="none"/><path d="M9 9l4 4" stroke="#fff" stroke-width="2"/></svg>VIEW</div>
    <div class="testi-brand">Norvalis <i></i></div>
    <p class="testi-text">Excellent work and very professional. Marcus takes time to explain everything and demonstrate workings. Very clear precise and accurate.</p>
  </div>
  <div class="testi-name"><b>Jensa</b><span>Norvalis / Cranbourne North VIC</span></div>
</section>

<section class="sec logos">
  <div class="and-more">and<br>more...</div>
  <div class="logo-tile light">Velvetia</div>
  <div class="logo-tile soft">Outback Supply</div>
  <div class="logo-tile dark">Heron Plumbing</div>
  <div class="logo-tile dark">Goldarch</div>
</section>

<section class="sec contact">
  <h2 class="heading">Questions? <span class="hl">Contact Us!</span></h2>
  <div class="field" style="left:145px;top:142px;width:228px">Name*</div>
  <div class="field" style="left:448px;top:142px;width:305px">Company</div>
  <div class="field" style="left:757px;top:142px;width:298px">Email*</div>
  <div class="field" style="left:145px;top:185px;width:228px">Phone</div>
  <div class="field select" style="left:448px;top:185px;width:305px">Purpose</div>
  <div class="field" style="left:757px;top:185px;width:298px">Address</div>
  <div class="field" style="left:145px;top:229px;width:910px;height:142px">Message*</div>
  <span class="btn-red"><span>Send a Message ›</span></span>
</section>

<section class="sec info">
  <svg class="info-bg" width="1200" height="157"><polygon points="0,30 1200,0 1200,157 0,157" fill="#f3f3f3"/></svg>
  <div class="info-item" style="left:145px">
    <div class="info-ico"><svg width="22" height="30" viewBox="0 0 22 30"><path d="M11 1C5 1 1 5 1 11c0 8 10 18 10 18s10-10 10-18C21 5 17 1 11 1z" fill="#1d1d1f"/><circle cx="11" cy="11" r="4" fill="#fff"/></svg></div>
    <div><h5>Visit</h5><p>22/84 Larkin Rd<br>Glen Ashby, VIC3152</p></div>
  </div>
  <div class="info-item" style="left:458px">
    <div class="call-label">CALL</div>
    <div class="phone" style="position:static">
      <svg width="40" height="30" viewBox="0 0 40 30"><path d="M3 10c0-6 34-6 34 0v4h-9v-4c0-2-16-2-16 0v4H3z" fill="#1d1d1f"/><rect x="8" y="14" width="24" height="14" rx="3" fill="#1d1d1f"/><circle cx="20" cy="21" r="4" fill="#fff"/></svg>
      <div class="num"><span class="d">13 </span><span class="r">7260</span></div>
    </div>
  </div>
  <div class="info-item" style="left:768px">
    <div class="info-ico"><svg width="28" height="20" viewBox="0 0 28 20"><rect x="1" y="1" width="26" height="18" fill="#1d1d1f"/><path d="M1 1l13 10L27 1" stroke="#fff" stroke-width="2" fill="none"/></svg></div>
    <div><h5>Email</h5><p>service@tavoelectrical.com.au</p></div>
  </div>
</section>

<footer>
  <nav class="sec footer-nav">
    <ul><li>Electrical</li><li>LED Lighting</li><li>Solar Power</li><li class="plain">Career</li><li class="plain">Terms &amp; Conditions</li><li class="plain">Privacy</li></ul>
    <div class="social"><i></i><i class="c"></i><i></i></div>
  </nav>
  <div class="sec copyright">©2017 Tavo Electrical. All rights reserved.</div>
</footer>

</body>
</html>
```